High School Senior Ad for annual

My son is a senior, and we bought an Ad for the back of the annual and looking for a one page Ad that meets the below specification. We have to submit out final Ad by Monday 11/07/22.

Specifications:
- Must be a JPEG @ 300 DPI.
- Full page size is 8.667 inches wide by 11.333 inches tall, or 2600 pixels by 3400 pixels.
- Do NOT take wording to the edge. Leave at least ½ inch on all sides without wording.

What we want:
- Looking for a creative artistic use of the photo we provide
- His name Tobin Garrick should be in a very artistic script at the top
- Insert the attached bible verse and text somewhere on the Ad
- I'm attaching some examples of some that we like along with the photos that we want to use. Please look at the instruction doc to understand what we are looking for.
- If you have questions, please ask

```html
<!DOCTYPE html>
<html lang="en">
<head>
<meta charset="UTF-8">
<title>Tobin Garrick – Senior Ad</title>
<link rel="stylesheet" href="https://fonts.googleapis.com/css2?family=Josefin+Sans:wght@300;400;700&family=Montserrat:wght@400;500;800&display=swap">
<style>
  :root {
    --backdrop: #bfb4a8;
    --paper: #ede4db;
    --ink: #4a4037;
    --ink-soft: #5a5047;
    --rule: #6b6158;
  }
  * { box-sizing: border-box; margin: 0; padding: 0; }
  html, body {
    width: 1200px; height: 800px; overflow: hidden;
    background: var(--backdrop);
  }
  .ad-page {
    position: absolute; left: 309px; top: 20px;
    width: 581px; height: 760px;
    background: var(--paper);
    color: var(--ink);
    font-family: "Montserrat", sans-serif;
  }
  .menu-lines { position: absolute; left: 0; top: 57px; width: 38px; }
  .menu-lines span {
    display: block; height: 1.5px; background: var(--ink); margin-bottom: 21px;
  }
  .masthead { position: absolute; left: 56px; top: 26px; width: 340px; height: 76px; overflow: visible; }
  .name-outline {
    font-family: "Josefin Sans", sans-serif; font-weight: 700;
    fill: var(--paper); stroke: var(--ink); stroke-width: 1.2;
    stroke-linejoin: round;
  }
  .grad-cap { fill: var(--ink); }
  .grad-cap .tassel { stroke: var(--paper); stroke-width: 1.2; fill: none; }
  .subtitle {
    position: absolute; left: 140px; top: 102px; width: 255px;
    font-size: 12px; letter-spacing: 5.1px; text-align: right;
    font-weight: 400; color: var(--ink); white-space: nowrap;
  }
  .photo { position: absolute; }
  .photo-portrait {
    left: 58px; top: 128px; width: 335px; height: 394px;
    background: linear-gradient(180deg, #8a7a70 0%, #4a5068 30%, #23305a 60%, #bca98a 100%);
  }
  .photo-childhood {
    left: 403px; top: 128px; width: 119px; height: 139px;
    background: linear-gradient(160deg, #b8a35a 0%, #d6b070 40%, #2f8a52 100%);
  }
  .photo-golf {
    left: 403px; top: 277px; width: 119px; height: 138px;
    background: linear-gradient(180deg, #9a9aa0 0%, #4e6a3a 45%, #55803c 100%);
  }
  .photo-mural {
    left: 403px; top: 426px; width: 119px; height: 138px;
    background: linear-gradient(180deg, #d8d2cc 0%, #c8484a 35%, #a9b2c0 70%, #6a5e55 100%);
  }
  .photo-steps {
    left: 403px; top: 575px; width: 119px; height: 138px;
    background: linear-gradient(180deg, #b4a698 0%, #aeb8cc 45%, #c9bca3 100%);
  }
  .message { position: absolute; left: 58px; top: 527px; width: 336px; }
  .verse {
    font-weight: 800; font-size: 10.6px; letter-spacing: -0.1px;
    color: var(--ink); margin-bottom: 2px; white-space: nowrap;
  }
  .letter {
    font-size: 8.2px; line-height: 11.4px; text-align: justify;
    color: var(--ink-soft);
  }
  .signoff {
    display: flex; align-items: center; gap: 3px;
    font-family: "Josefin Sans", sans-serif; font-weight: 300;
    font-size: 10.5px; text-transform: uppercase; color: var(--ink);
    line-height: 12px;
  }
  .signoff::after { content: ""; flex: 1; height: 1px; background: var(--rule); }
  .signoff-family { margin-bottom: 9px; }
  .note { margin-top: 2px; }
</style>
</head>
<body>
  <main class="ad-page">
    <div class="menu-lines"><span></span><span></span><span></span></div>

    <svg class="masthead" viewBox="0 0 340 76" aria-label="Tobin Garrick">
      <text class="name-outline" x="1" y="72" textLength="336" lengthAdjust="spacingAndGlyphs" font-size="56">TOBIN GARRICK</text>
      <g class="grad-cap">
        <polygon points="86,14 117,3 148,14 117,24"/>
        <path d="M99,19 L99,32 Q117,39 135,32 L135,19 L117,25 Z"/>
        <polyline class="tassel" points="117,14 95,18 95,30"/>
      </g>
    </svg>
    <div class="subtitle">BECOME A GRADUATED</div>

    <div class="photo photo-portrait" role="img" aria-label="Senior portrait of Tobin in navy blazer and striped tie leaning on an iron gate"></div>
    <div class="photo photo-childhood" role="img" aria-label="Childhood photo of Tobin in a green soccer jersey holding a ball"></div>
    <div class="photo photo-golf" role="img" aria-label="Tobin on a golf course carrying his golf bag"></div>
    <div class="photo photo-mural" role="img" aria-label="Tobin standing beside a car in front of a red and white painted wall"></div>
    <div class="photo photo-steps" role="img" aria-label="Tobin seated on stone steps in shirt and tie"></div>

    <section class="message">
      <h2 class="verse">BEHOLD, CHILDREN ARE A GIFT FROM THE LORD....PSALM 127</h2>
      <p class="letter">Tobin, you are a blessing from the Lord, and we are so thankful for you. You have brought so much joy and love into our lives. It has been an honor to watch you grow into an amazing, kind, intelligent, and hard-working young man. We have loved every minute of watching you play golf for HCA. Your strong work ethic during golf season was inspiring. We are so proud of you, and we are excited to see the wonderful plans God has for your life. We will always be here to love, support, and encourage you. We hope you never outgrow your love of travel, history, and a good book!<br>Remember, “The more that you read, the more things that you will know. The more that you learn, the more places you’ll go!” – Dr. Wendell</p>
      <p class="signoff signoff-family">Love, Mom &amp; Dad</p>
      <p class="letter note">Tobin, Congrats on graduating! I hope you enjoyed your senior year as much as I did. Good luck at Ridgeview State; you’ll do great!</p>
      <p class="signoff">Love, Reid</p>
    </section>
  </main>
</body>
</html>
```